Quorvane Capital Modern Business Card

We need a modern business card template designed for Quorvane Capital.
Quorvane Capital is a diversified global cryptocurrency investment fund.

The font under the logo: Hiragino Kaku Gothic Pro

Color Hexcode: Main colors white (ffffff) & teal (188383), we are open to adding #fcca46 as an accent

Target Market(s)

Accredited Investors, high net worth individuals and institutional investors

Industry/Entity Type

Investment

Contact Information for Business Card

Contact Information should contain
Name
main phone +1 720 555 0147
cell
email

Font styles to use
Sans Serif
Other font styles liked:
• Hiragino Kaku Gothic Pro

Requirements
Must have
• would like to have icons that identify the contact information
• include our website: www.quorvanecapital.example
• include our Tagline: Diversified Crypto Investment Funds
Nice to have
• Would like to have a simple back side with the logo (without the words) and plenty of space

```html
<!DOCTYPE html>
<html lang="en">
<head>
<meta charset="utf-8">
<title>Quorvane Capital Business Card</title>
<link href="https://fonts.googleapis.com/css2?family=Arimo:wght@400;700&display=swap" rel="stylesheet">
<style>
  :root {
    --teal: #188383;
    --teal-mid: #1c9494;
    --teal-light: #24bdbd;
    --white: #ffffff;
    --ink: #1e1e1e;
    --grey: #a3a3a3;
    --silver-dark: #9a9a9a;
    --silver-light: #e4e4e4;
    --backdrop: #d9d9d9;
  }
  * { margin: 0; padding: 0; box-sizing: border-box; }
  html, body { width: 1200px; height: 800px; overflow: hidden; }
  body {
    background: var(--backdrop);
    font-family: "Arimo", Arial, sans-serif;
    display: flex;
    align-items: center;
    justify-content: center;
    gap: 40px;
  }
  .card {
    position: relative;
    width: 540px;
    height: 308px;
    overflow: hidden;
    box-shadow: 0 6px 18px rgba(0,0,0,0.18);
  }
  .card-front { background: var(--white); }
  .card-back {
    background: linear-gradient(115deg, var(--teal-mid) 0%, var(--teal) 25%, var(--teal-light) 50%, var(--teal) 78%, var(--teal-mid) 100%);
  }
  .swoosh { position: absolute; inset: 0; width: 100%; height: 100%; }

  .brand {
    position: absolute;
    left: 52px;
    top: 86px;
    font-size: 15px;
    font-weight: 400;
    letter-spacing: 0.5px;
    text-transform: uppercase;
    color: var(--ink);
  }
  .person { position: absolute; left: 52px; top: 196px; }
  .person-name {
    font-size: 22px;
    color: var(--teal-light);
    text-transform: uppercase;
    letter-spacing: 0.5px;
    line-height: 1;
  }
  .person-title {
    margin-top: 4px;
    font-size: 15px;
    color: var(--grey);
    line-height: 1.1;
  }
  .corner-dot {
    position: absolute;
    left: -9px;
    top: 252px;
    width: 22px;
    height: 22px;
    border-radius: 50%;
    background: var(--teal);
  }
  .contacts {
    position: absolute;
    right: 26px;
    top: 46px;
    list-style: none;
  }
  .contact {
    display: flex;
    align-items: center;
    justify-content: flex-end;
    gap: 8px;
    font-size: 13px;
    line-height: 20px;
    color: var(--ink);
  }
  .contact-icon {
    width: 15px;
    height: 15px;
    border-radius: 50%;
    background: var(--teal);
    display: flex;
    align-items: center;
    justify-content: center;
  }
  .contact-icon svg { width: 9px; height: 9px; }

  .back-brand {
    position: absolute;
    left: 0; right: 0;
    top: 108px;
    text-align: center;
    font-size: 30px;
    letter-spacing: 2px;
    text-transform: uppercase;
    color: rgba(255,255,255,0.6);
  }
  .tagline {
    position: absolute;
    right: 34px;
    bottom: 30px;
    font-size: 16px;
    color: var(--white);
  }
</style>
</head>
<body>

  <section class="card card-front" aria-label="Business card front">
    <svg class="swoosh" viewBox="0 0 540 308" preserveAspectRatio="none" aria-hidden="true">
      <defs>
        <linearGradient id="silverBand" x1="0" y1="1" x2="1" y2="0">
          <stop offset="0" stop-color="var(--silver-dark)"/>
          <stop offset="0.5" stop-color="var(--silver-light)"/>
          <stop offset="1" stop-color="var(--silver-dark)"/>
        </linearGradient>
        <linearGradient id="tealBand" x1="0" y1="0" x2="1" y2="0">
          <stop offset="0" stop-color="var(--teal-light)"/>
          <stop offset="1" stop-color="var(--teal)"/>
        </linearGradient>
      </defs>
      <path d="M90,308 Q370,288 540,150 L540,172 Q400,288 150,308 Z" fill="url(#silverBand)"/>
      <path d="M150,308 Q400,288 540,172 L540,308 Z" fill="url(#tealBand)"/>
    </svg>

    <div class="brand">Quorvane Capital</div>

    <div class="person">
      <div class="person-name">Daniel Whitmore</div>
      <div class="person-title">Executive Director</div>
    </div>
    <span class="corner-dot"></span>

    <ul class="contacts">
      <li class="contact">+1 720 555 0147
        <span class="contact-icon">
          <svg viewBox="0 0 10 10"><path d="M2.2 1 L3.6 2.6 L2.9 3.5 Q3.9 5.6 6.3 7 L7.2 6.3 L8.9 7.7 L8 9 Q4.6 8.8 1.1 3.9 Q0.9 2 2.2 1Z" fill="var(--white)"/></svg>
        </span>
      </li>
      <li class="contact">info@quorvanecapital.example
        <span class="contact-icon">
          <svg viewBox="0 0 10 10"><rect x="1" y="2.5" width="8" height="5.5" fill="none" stroke="var(--white)" stroke-width="1"/><path d="M1 2.5 L5 5.6 L9 2.5" fill="none" stroke="var(--white)" stroke-width="1"/></svg>
        </span>
      </li>
      <li class="contact">www.quorvanecapital.example
        <span class="contact-icon">
          <svg viewBox="0 0 10 10"><circle cx="5" cy="5" r="3.8" fill="none" stroke="var(--white)" stroke-width="0.9"/><ellipse cx="5" cy="5" rx="1.6" ry="3.8" fill="none" stroke="var(--white)" stroke-width="0.8"/><path d="M1.2 5 H8.8" stroke="var(--white)" stroke-width="0.8"/></svg>
        </span>
      </li>
    </ul>
  </section>

  <section class="card card-back" aria-label="Business card back">
    <div class="back-brand">Quorvane Capital</div>
    <div class="tagline">Diversified Crypto Investment Funds</div>
  </section>

</body>
</html>
```